Manufacturing company needs new business card.

I need a unique Business Card that will truly stand out. Nothing too busy. Simple is good, right? Not looking for a standard design either. No cookie cutter layout. I am just looking for something interesting and a bit different. Does't have to completely off the wall crazy, just not your run of the mill business card. Clean and modern with a touch of industrial.

Target Market(s)

Air conditioning industry, Architects, builders.

Industry/Entity Type

Business

Contact Information for Business Card

Details to be included on card are:

Peter Vance
Managing Director

T: 1300 847 519
M: 0428 593 174
W: www.brenvaleworks.com.au
E: peter.vance@brenvaleworks.com.au
A: 58 Harwick Lane, Sydney NSW 2000

Font styles to use
Sans Serif

Colors
0355a3
848484
fbfbfb

Requirements
Must have
• Card design must be landscape.

```html
<!DOCTYPE html>
<html lang="en">
<head>
<meta charset="utf-8">
<title>Brenvale Works – Business Card</title>
<link href="https://fonts.googleapis.com/css2?family=Source+Sans+3:wght@400;600;700&display=swap" rel="stylesheet">
<style>
  :root {
    --brand-blue: #0355a3;
    --card-blue: #2d5cb4;
    --steel-grey: #848484;
    --paper: #fbfbfb;
    --ink: #1d1d1f;
    --backdrop: #e4e4e4;
  }
  * { box-sizing: border-box; margin: 0; padding: 0; }
  html, body { width: 1133px; height: 1200px; overflow: hidden; }
  body {
    background: var(--backdrop);
    font-family: "Source Sans 3", Arial, sans-serif;
    position: relative;
  }
  .card {
    position: absolute;
    left: 156px;
    width: 820px;
    height: 500px;
    border-radius: 26px;
    overflow: hidden;
    box-shadow: 0 8px 24px rgba(0,0,0,.18);
  }
  .card--front { top: 60px; background: var(--paper); }
  .card--back { top: 640px; background: var(--card-blue); }

  .front-bands { position: absolute; inset: 0; }

  .wordmark {
    position: absolute;
    display: flex;
    align-items: center;
    gap: 14px;
    font-weight: 600;
    font-size: 40px;
    letter-spacing: .5px;
    white-space: nowrap;
  }
  .wordmark__square { width: 30px; height: 30px; border-radius: 4px; }
  .card--front .wordmark { right: 70px; top: 70px; color: var(--brand-blue); }
  .card--front .wordmark__square { background: var(--brand-blue); }
  .card--back .wordmark { right: 64px; bottom: 70px; color: #ffffff; }
  .card--back .wordmark__square { background: var(--steel-grey); }

  .person { position: absolute; left: 40px; top: 196px; }
  .person__name { color: #ffffff; font-size: 42px; font-weight: 400; line-height: 1; }
  .person__name strong { font-weight: 700; }
  .person__title { color: var(--brand-blue); font-size: 24px; margin-top: 16px; }

  .contacts { position: absolute; left: 40px; top: 318px; list-style: none; }
  .contacts li {
    display: flex; align-items: center; gap: 14px;
    font-size: 23px; color: var(--ink); line-height: 31px;
  }
  .contacts svg { width: 20px; height: 20px; fill: var(--brand-blue); flex: none; }
</style>
</head>
<body>

<section class="card card--front" aria-label="Business card front">
  <svg class="front-bands" viewBox="0 0 820 500" preserveAspectRatio="none" aria-hidden="true">
    <polygon points="0,140 240,140 285,188 0,188" fill="#848484"/>
    <polygon points="0,188 260,188 270,168 820,168 820,205 300,205 288,255 0,255" fill="#0355a3"/>
  </svg>

  <div class="wordmark"><span class="wordmark__square"></span>Brenvale Works</div>

  <div class="person">
    <p class="person__name">Peter <strong>Vance</strong></p>
    <p class="person__title">Managing Director</p>
  </div>

  <ul class="contacts">
    <li><svg viewBox="0 0 24 24"><path d="M3 9c0-3 4-5 9-5s9 2 9 5v2h-5V9H8v2H3z M6 12h12l2 8H4z"/></svg>1300 847 519</li>
    <li><svg viewBox="0 0 24 24"><path d="M7 1h10a2 2 0 0 1 2 2v18a2 2 0 0 1-2 2H7a2 2 0 0 1-2-2V3a2 2 0 0 1 2-2zm0 3v14h10V4zm5 15.5a1 1 0 1 0 0 2 1 1 0 0 0 0-2z"/></svg>0428 593 174</li>
    <li><svg viewBox="0 0 24 24"><path d="M12 2a10 10 0 1 0 0 20 10 10 0 0 0 0-20zm0 2c1.2 1.3 2 3.5 2.3 7H9.7c.3-3.5 1.1-5.7 2.3-7zM4.1 11a8 8 0 0 1 4-6.2c-.7 1.6-1.2 3.7-1.4 6.2zm0 2h2.6c.2 2.5.7 4.6 1.4 6.2A8 8 0 0 1 4.1 13zm5.6 0h4.6c-.3 3.5-1.1 5.7-2.3 7-1.2-1.3-2-3.5-2.3-7zm6.2 6.2c.7-1.6 1.2-3.7 1.4-6.2h2.6a8 8 0 0 1-4 6.2zM17.3 11c-.2-2.5-.7-4.6-1.4-6.2a8 8 0 0 1 4 6.2z"/></svg>www.brenvaleworks.com.au</li>
    <li><svg viewBox="0 0 24 24"><path d="M2 5h20v14H2zm2 2v.5l8 5.5 8-5.5V7zm0 3v7h16v-7l-8 5.5z"/></svg>peter.vance@brenvaleworks.com.au</li>
    <li><svg viewBox="0 0 24 24"><path d="M12 1a7 7 0 0 0-7 7c0 5.3 7 15 7 15s7-9.7 7-15a7 7 0 0 0-7-7zm0 9.5a2.5 2.5 0 1 1 0-5 2.5 2.5 0 0 1 0 5z"/></svg>58 Harwick Lane, Sydney NSW 2000</li>
  </ul>
</section>

<section class="card card--back" aria-label="Business card back">
  <div class="wordmark"><span class="wordmark__square"></span>Brenvale Works</div>
</section>

</body>
</html>
```